Tidy Haven Path half fold brochure design

I need a brochure for a new company. The name of the company is Tidy Haven Path. I am a Professional Organizer. I am requesting a one fold brochure 11" wide x 8.5" high (obviously once folded 5.5" wide x 8.5" high) brochure. I have been told this may need to be designed as a flyer? I have attached a VERY BASIC layout of what I think I am looking for. I have also attached the original logos in all the different formats I have. I would like to have a very light green background & the text I have in orange please make orange. PLEASE feel free to add color to my "Tidy Haven Path" logo's and use light/soft green & orange shades if possible (OK to go darker for BOLD purposes) The brochure DOES NOT have to stick to this layout, again just what I THINK I want :) - THANK YOU

EDIT: 01-21-15 Remove MARLENE KUDSIK from all 3 places (front, bottom inside right & back) Remove just the KUDSIK from the 1st line on the back. PRIVACY & ETHICS on the back, please remove "PRIVACY &", leave Ethics and the 1st line of the text under it. Please remove all of the text following the 1st sentence. THANK YOU

Industry/Entity Type

It Company

```html
<!DOCTYPE html>
<html lang="en">
<head>
<meta charset="utf-8">
<title>Tidy Haven Path – Brochure</title>
<link href="https://fonts.googleapis.com/css2?family=Open+Sans:wght@300;400;700&family=Source+Sans+3:ital,wght@0,400;0,600;0,700;1,400&display=swap" rel="stylesheet">
<style>
  :root{
    --orange:#f7941d;
    --green:#a6ce5a;
    --slate:#4a4a4c;
    --ink:#3a3a3a;
    --paper:#f3f8e8;
    --badge:#d9dcd2;
    --backdrop:#ffffff;
  }
  *{margin:0;padding:0;box-sizing:border-box}
  html,body{width:810px;height:1200px;overflow:hidden;background:var(--backdrop)}
  body{font-family:"Source Sans 3","Myriad Pro",Arial,sans-serif;color:var(--ink)}
  .stage{position:absolute;left:0;top:0;width:900px;height:1334px;transform:scale(.9);transform-origin:0 0}
  .sheet{position:absolute;left:52px;width:791px;height:612px;background:var(--paper);box-shadow:3px 4px 6px rgba(0,0,0,.45);overflow:hidden}
  .sheet--outside{top:40px}
  .sheet--inside{top:683px}
  .block{position:absolute}
  .block--orange{background:var(--orange)}
  .block--green{background:var(--green)}
  .block--slate{background:var(--slate);color:#fff;font-family:"Open Sans",Arial,sans-serif;font-weight:300}
  .photo{position:absolute}

  .clarity-title{padding:40px 0 0 24px;line-height:1.1}
  .clarity-title .big{font-size:30px;display:block;margin-bottom:2px}
  .clarity-title .small{font-size:17px;display:block;line-height:20px}
  .services-title{padding:50px 14px 0 0;text-align:right;font-size:25px;line-height:30px}

  .badge{position:absolute;left:160px;top:330px;width:72px;height:72px;background:var(--badge)}
  .contact{position:absolute;left:122px;top:477px;color:var(--orange);font-size:13px;line-height:15.5px}
  .contact p{margin-bottom:6px}

  .brand{position:absolute;left:500px;top:395px;width:200px;display:flex;align-items:center;gap:10px;color:var(--orange);font-weight:700;font-size:32px;line-height:1.0}
  .brand__mark{width:18px;height:18px;border-radius:50%;background:var(--green);flex:none}

  .col{position:absolute;font-size:10px;line-height:11.5px}
  .col h2{color:var(--orange);font-size:12.5px;font-weight:700;margin-bottom:5px;line-height:13.5px}
  .col h3{color:var(--orange);font-size:11.5px;font-weight:700;margin:7px 0 4px;line-height:12.5px}
  .col p{margin-bottom:6px}
  .col .cite{font-style:italic;text-align:right;font-size:9.5px}
  .col .closing{color:var(--orange);font-weight:700;font-size:11px;line-height:12.5px}

  .tagline{padding:22px 18px 0 0;text-align:right;font-size:25px;line-height:30px}
</style>
</head>
<body>
<div class="stage">

  <section class="sheet sheet--outside" aria-label="Outside cover">
    <div class="block block--orange" style="left:0;top:0;width:96px;height:99px"></div>
    <div class="block block--green" style="left:105px;top:0;width:185px;height:99px"></div>
    <div class="photo" role="img" aria-label="Photo of a cluttered workbench with an old sewing machine" style="left:299px;top:0;width:185px;height:99px;background:linear-gradient(160deg,#6d5a4c,#2f2a27)"></div>
    <div class="block block--orange" style="left:493px;top:0;width:185px;height:99px"></div>
    <div class="block block--green" style="left:687px;top:0;width:104px;height:99px"></div>

    <div class="photo" role="img" aria-label="Photo of a cluttered office room" style="left:0;top:108px;width:96px;height:194px;background:linear-gradient(170deg,#b5a08a,#6e6258)"></div>
    <div class="block block--slate clarity-title" style="left:105px;top:108px;width:185px;height:194px">
      <span class="big">Clarity:</span>
      <span class="small">The</span>
      <span class="small">Quality or State</span>
      <span class="small">of Being Clear</span>
    </div>
    <div class="photo" role="img" aria-label="Photo of a frustrated woman overwhelmed by clutter" style="left:299px;top:108px;width:185px;height:194px;background:linear-gradient(180deg,#6a5448,#a07a64)"></div>
    <div class="block block--slate services-title" style="left:493px;top:108px;width:185px;height:194px">Organizing &amp;<br>Decluttering<br>Services</div>
    <div class="photo" role="img" aria-label="Photo of a cluttered kitchen with a stove" style="left:687px;top:108px;width:104px;height:194px;background:linear-gradient(180deg,#a5865f,#d7cfc2)"></div>

    <div class="photo" role="img" aria-label="Photo of a messy bedroom with piled clothes" style="left:0;top:311px;width:96px;height:194px;background:linear-gradient(170deg,#c9b99c,#8a7a86)"></div>
    <div class="block block--orange" style="left:299px;top:311px;width:185px;height:194px"></div>
    <div class="photo" role="img" aria-label="Photo of a crowded kitchen counter" style="left:687px;top:311px;width:104px;height:194px;background:linear-gradient(180deg,#b59a7a,#7e6a58)"></div>

    <div class="block block--green" style="left:0;top:514px;width:96px;height:98px"></div>
    <div class="photo" role="img" aria-label="Photo of tangled holiday ornaments" style="left:299px;top:514px;width:185px;height:98px;background:linear-gradient(135deg,#b88a3a,#8c2a22)"></div>
    <div class="photo" role="img" aria-label="Photo of a shelf crammed with pots and pans" style="left:493px;top:514px;width:185px;height:98px;background:linear-gradient(180deg,#6b4a3a,#3c3230)"></div>
    <div class="block block--orange" style="left:687px;top:514px;width:104px;height:98px"></div>

    <div class="badge" role="img" aria-label="Membership badge"></div>

    <div class="contact">
      <p>301-555-0148</p>
      <p style="margin-bottom:0">info@tidyhavenpath.com</p>
      <p>www.tidyhavenpath.com</p>
      <p style="margin-bottom:0">Fairview, MD</p>
      <p>Serving MD, DC &amp; VA</p>
    </div>

    <div class="brand"><span class="brand__mark"></span><span>Tidy Haven Path</span></div>
  </section>

  <section class="sheet sheet--inside" aria-label="Inside spread">
    <div class="col" style="left:23px;top:34px;width:166px">
      <h2>HELLO!</h2>
      <p>My name is Marlene. I offer simple, fun and insightful solutions to seemingly complicated clutter and organizational problems. I am here to help if you are ready to change your home and/or workspace.</p>
      <p>My experiences of working with family, friends, co-workers and clients has proven my hard working, energetic, fun and supportive attitude makes it easier for them to get things accomplished. Helping people sort through, and be rid of, the mental and physical obstacles that have kept them stuck along with participating in their enthusiasm when they see immediate improvement is rewarding for me.</p>
      <p>I welcome the opportunity to earn your confidence through ethical, reliable and dependable hard work.</p>
    </div>
    <div class="block block--slate tagline" style="left:0;top:310px;width:185px;height:194px">Together we<br>can conquer<br>the clutter<br>and create<br>CLARITY</div>
    <div class="block block--green" style="left:0;top:511px;width:185px;height:101px"></div>

    <div class="col" style="left:204px;top:34px;width:166px">
      <h2>GETTING ORGANIZED</h2>
      <p>It isn’t all about everything being in its proper place.</p>
      <p>It can also require overcoming fears and anxieties such as:</p>
      <h3>How do I start?</h3>
      <p>You begin by getting help from a professional. No one can do everything; everyone needs a helping hand at times. (I bring my vehicle to a mechanic when it needs service, even for just a simple oil change!)</p>
      <h3>Am I going to have to get rid of ALL my things?</h3>
      <p>Definitely not! There is a process that will help you decide what to keep and what you would be willing to part with. (I can help you determine the practical and monetary “worth” of something. Only you can determine its personal “value”.)</p>
      <h3>I don’t have time</h3>
      <p>Now you will! Getting organized will actually save you time. You will know where that “thing” is, find it quickly and avoid the time it takes to run out and purchase a new “thing”. (You will have actually created more time to enjoy the lifestyle that is important to you.)</p>
      <p>We all have anxiety about something that prevents or inhibits us from taking action toward a solution. Whether you want someone to take over the project or a helping hand (nudge) is all you really need, a professional organizer is the perfect way to get started. Getting organized is going to be a process of progress, not perfection. It will require some level of support and continued work on you part, but the rewards will far outweigh the efforts.</p>
    </div>

    <div class="block block--orange" style="left:395px;top:0;width:185px;height:97px"></div>
    <div class="photo" role="img" aria-label="Photo of colorful shirts on hangers" style="left:395px;top:107px;width:185px;height:195px;background:linear-gradient(90deg,#2f6f8a,#c9c1b0 50%,#e0792e)"></div>
    <div class="photo" role="img" aria-label="Photo of a tidy desk with lamp and laptop" style="left:395px;top:310px;width:185px;height:194px;background:linear-gradient(180deg,#e6e3de,#bdb7ae)"></div>
    <div class="photo" role="img" aria-label="Photo of wooden tree and star ornaments" style="left:395px;top:511px;width:185px;height:101px;background:linear-gradient(90deg,#7a3a7a,#a0569a)"></div>

    <div class="col" style="left:604px;top:34px;width:170px">
      <h2>WHAT IS A PROFESSIONAL ORGANIZER?</h2>
      <p>“A Professional Organizer enhances the lives of clients by designing systems and processes using organizing principles and through transferring organizing skills. Professional Organizers help individuals and businesses take control of their surroundings, their time, their paper, and their systems for life.”</p>
      <p class="cite">Guild of Home<br>Organizers</p>
      <h2 style="margin-top:16px">SERVICES:</h2>
      <p>Whether you are too busy, too confused, over whelmed, tired, stressed or just don’t know where to start, I offer a variety of hands on services to help you bring a sense of fun, freedom and functionality to almost any space.</p>
      <h3>ATTIC–TO–BASEMENT:</h3>
      <p>Sorting - Purging - Organizing</p>
      <h3>PAPER CONTROL:</h3>
      <p>Sorting - Purging - Organizing. Household, home office &amp; home based filing systems</p>
      <h3>DOWNSIZING:</h3>
      <p>Sorting - purging - organizing - labeling. Packing &amp; unpacking</p>
      <h3>REMOVAL:</h3>
      <p>Light trash &amp; proper disposal. Donations &amp; light recyclables to proper locations. Shredding Service</p>
      <h3>FOLLOW UP:</h3>
      <p>Routine “clutter maintenance” visits.</p>
      <p class="closing">For projects not listed above, please contact me.</p>
    </div>
  </section>

</div>
</body>
</html>
```